Business Card Design

We need a business card design for our new expansion based in Bloomfield Hills, Michigan. Our company is Quiet Harbor Institute & Wellness Center. Our Academy teaches individuals of all ages and professions to live from their soul. We teach intuitive development, meditation and mindfulness; shamanic healing. And ourr healing center provides holistic services. We offer certification programs that support the ethical practices of Intuitive professionals. Our team of Intuitive Practitioners includes: doctors, psychologists, chiropractor, soul retrievers, mediums, etc who all balance their knowledge with intuitive wisdom.

We want our symbol to be the Blue Morpho Buttefly and the colors on the card to complement it. We want to communicate inspiration, healing and empowerment. Thank you

Industry/Entity Type

Business

Contact Information for Business Card

Dana Farrow
Medium. Author. Soul Retriever.
Founder, Quiet Harbor

Quiet Harbor

19 East Cedar Mill Drive Suite 200
Willow Bend, OH 48391
330-555-0174

www.danafarrowexample.com

Requirements
Must have
• blue morpho butterfly

```html
<!DOCTYPE html>
<html lang="en">
<head>
<meta charset="utf-8">
<title>Dana Farrow – Business Card</title>
<link href="https://fonts.googleapis.com/css2?family=Didact+Gothic&display=swap" rel="stylesheet">
<style>
  :root{
    --morpho:#00aeef;
    --paper:#ffffff;
    --ink:#3a3a3a;
    --ink-soft:#6d6d6d;
    --backdrop:#ececec;
  }
  *{box-sizing:border-box;margin:0;padding:0}
  html,body{width:1200px;height:919px;overflow:hidden}
  body{
    background:var(--backdrop);
    font-family:"Didact Gothic",sans-serif;
    display:flex;flex-direction:column;align-items:center;justify-content:center;gap:56px;
  }
  .card{
    width:630px;height:360px;position:relative;
    box-shadow:0 6px 18px rgba(0,0,0,.12);
  }
  /* back side */
  .card--back{
    background:var(--morpho);color:var(--paper);
    display:flex;flex-direction:column;align-items:center;justify-content:center;gap:26px;
  }
  .brand{display:flex;align-items:center;gap:14px}
  .brand__dot{width:30px;height:30px;border-radius:50%}
  .card--back .brand__dot{background:var(--paper)}
  .card--back .brand__name{font-size:48px;color:var(--paper)}
  .website{font-size:17px;letter-spacing:.32em;color:var(--paper)}
  /* front side */
  .card--front{background:var(--paper)}
  .card--front .brand{position:absolute;left:44px;top:50px}
  .card--front .brand__dot{background:var(--morpho);width:22px;height:22px}
  .card--front .brand__name{font-size:30px;color:var(--ink)}
  .identity{position:absolute;right:44px;top:118px;text-align:right}
  .identity__name{font-size:26px;color:var(--morpho);letter-spacing:.04em}
  .identity__degree{color:var(--ink)}
  .identity__role{font-size:15px;color:var(--ink-soft);letter-spacing:.06em;line-height:1.35}
  .contact{position:absolute;left:44px;bottom:52px;list-style:none;
    font-size:15px;color:var(--ink-soft);letter-spacing:.06em;line-height:1.4}
  .contact__item{display:flex;align-items:flex-start;gap:12px;margin-top:14px}
  .contact__icon{width:18px;height:18px;flex:none;margin-top:1px}
</style>
</head>
<body>
  <section class="card card--back" aria-label="Card back">
    <div class="brand">
      <span class="brand__dot"></span>
      <span class="brand__name">Dana Farrow</span>
    </div>
    <p class="website">www.danafarrowexample.com</p>
  </section>

  <section class="card card--front" aria-label="Card front">
    <div class="brand">
      <span class="brand__dot"></span>
      <span class="brand__name">Dana Farrow</span>
    </div>

    <div class="identity">
      <p class="identity__name">Dana Farrow<span class="identity__degree">, M.Ed.</span></p>
      <p class="identity__role">Mentor, Writer, Energy Guide</p>
      <p class="identity__role">Founder, Quiet Harbor</p>
    </div>

    <ul class="contact">
      <li class="contact__item">
        <svg class="contact__icon" viewBox="0 0 18 18" aria-hidden="true">
          <circle cx="9" cy="9" r="8" fill="none" stroke="var(--morpho)" stroke-width="1.4"/>
          <path d="M6.3 4.8c.5-.3 1 0 1.2.5l.5 1.2c.1.4 0 .7-.3.9l-.5.4c.4 1 1.1 1.8 2.1 2.3l.4-.5c.3-.3.6-.4 1-.2l1.2.5c.5.2.7.7.4 1.2l-.4.7c-.4.6-1.2.8-1.9.5-2.2-1-3.8-2.7-4.6-4.9-.2-.7 0-1.5.6-1.9z" fill="var(--morpho)"/>
        </svg>
        <span>330-555-0174</span>
      </li>
      <li class="contact__item">
        <svg class="contact__icon" viewBox="0 0 18 18" aria-hidden="true">
          <circle cx="9" cy="9" r="8" fill="none" stroke="var(--morpho)" stroke-width="1.4"/>
          <path d="M9 4a3 3 0 0 0-3 3c0 2.2 3 6 3 6s3-3.8 3-6a3 3 0 0 0-3-3zm0 4.2a1.2 1.2 0 1 1 0-2.4 1.2 1.2 0 0 1 0 2.4z" fill="var(--morpho)"/>
        </svg>
        <span>19 East Cedar Mill Drive, Suite 200<br>Willow Bend, OH 48391</span>
      </li>
    </ul>
  </section>
</body>
</html>
```